Business Card Design Project

I have just chosen a logo and would now like this designed onto a business card for my hair salon. I would like it to be classy not to busy and have a wow factor when people look at them
Has to Include on card:
Logo Design
And business details below
Kaycee-rae Whitlow (owner)
0481 726 304
Lmv@brindal.com.au
57 Corella Street Kinross Vale
Logo is now attached please provide designs
Hair

```html
<!DOCTYPE html>
<html lang="en">
<head>
<meta charset="utf-8">
<title>Velora Hair Studio – Business Card</title>
<link rel="stylesheet" href="https://fonts.googleapis.com/css2?family=Questrial&display=swap">
<style>
  :root {
    --backdrop: #3b3b3c;
    --card: #1c1c1e;
    --teal: #45bcc8;
    --pink: #e0317e;
    --grey: #9a9a9e;
  }
  * { margin: 0; padding: 0; box-sizing: border-box; }
  html, body { width: 1200px; height: 827px; overflow: hidden; }
  body {
    background: var(--backdrop);
    font-family: "Questrial", "Century Gothic", sans-serif;
    position: relative;
  }
  .card {
    position: absolute;
    top: 265px;
    width: 520px;
    height: 297px;
    background: var(--card);
    border-radius: 4px;
    box-shadow: 0 10px 24px rgba(0,0,0,0.45);
  }
  .card--front { left: 50px; }
  .card--back { left: 630px; }

  .front-mark {
    position: absolute;
    inset: 0;
    display: flex;
    align-items: center;
    justify-content: center;
    gap: 14px;
    color: var(--teal);
    font-size: 30px;
    letter-spacing: 3px;
    text-transform: uppercase;
  }
  .front-mark .dot {
    width: 14px; height: 14px;
    border-radius: 50%;
    background: var(--teal);
  }

  .brand {
    position: absolute;
    top: 58px;
    right: 34px;
    width: 210px;
    text-align: right;
    color: var(--pink);
    font-size: 30px;
    line-height: 1.1;
    letter-spacing: 2px;
    text-transform: uppercase;
  }

  .contact {
    position: absolute;
    left: 34px;
    bottom: 46px;
    color: var(--grey);
    font-size: 12.5px;
  }
  .contact .name {
    color: var(--teal);
    font-size: 15px;
    letter-spacing: 1px;
    text-transform: uppercase;
  }
  .contact .role { margin-bottom: 12px; font-size: 12.5px; }
  .contact ul { list-style: none; }
  .contact li {
    display: flex;
    align-items: center;
    gap: 6px;
    line-height: 16px;
  }
  .contact svg { width: 9px; height: 9px; fill: var(--pink); flex: none; }
</style>
</head>
<body>
  <section class="card card--front" aria-label="Card front">
    <div class="front-mark"><span class="dot"></span>Velora</div>
  </section>

  <section class="card card--back" aria-label="Card back">
    <div class="brand">Velora Hair Studio</div>

    <div class="contact">
      <p class="name">Kaycee-rae Whitlow</p>
      <p class="role">Owner</p>
      <ul>
        <li>
          <svg viewBox="0 0 10 10" aria-hidden="true"><path d="M2 0.5l2 2-1 1.2c.6 1.3 1.6 2.3 2.9 2.9l1.2-1 2 2-1.3 1.6C4 9 1 6 0.5 1.7z"/></svg>
          0481 726 304
        </li>
        <li>
          <svg viewBox="0 0 10 10" aria-hidden="true"><path d="M0 2h10v6H0z M0 2l5 3.5L10 2" stroke="#1c1c1e" stroke-width="0.8"/></svg>
          Lmv@brindal.com.au
        </li>
        <li>
          <svg viewBox="0 0 10 10" aria-hidden="true"><path d="M5 0a3.5 3.5 0 0 1 3.5 3.5C8.5 6 5 10 5 10S1.5 6 1.5 3.5A3.5 3.5 0 0 1 5 0zm0 2.2a1.3 1.3 0 1 0 0 2.6 1.3 1.3 0 0 0 0-2.6z"/></svg>
          57 Corella Street Kinross Vale
        </li>
      </ul>
    </div>
  </section>
</body>
</html>
```